Coffee - Forum Design

Guarantee Payment:
I will start this project without guaranteeing payment. Until I receive 3 interested Freelancers emailing me "ready to start work", then I will guarantee payment.

About my website:
It will be a forum based website catering towards coffee and the like.

Requirements:
This will be a fun and simple design task. It requires the freelancer to take the dimensions of the following website:
https://brightlanehub.example/forums/
Please use the above website as your template.

And re-design it to suit my needs. Every single element in that the website above will be exactly the same. You can add personal touches to the design.

Theme:
Something fun and playful with a slight modern feel. Simple colours, nothing too crazy and bold. Preferably no dark colours.

Logo:
Is currently being finished off. Will be uploading in due course.

Thanks everyone and Good Luck,
Gord
PS. Send me a message if you have any queries.

NOTE: The PSD file must be CSS friendly while slicing the template.

Target Market(s)

Coffee & Cafe lovers of all types

Industry/Entity Type

Catering

Requirements
Must have
• Dimensions for each elements of the website can be seen in the following website, please use this as a guide:

```html
<!DOCTYPE html>
<html lang="en">
<head>
<meta charset="utf-8">
<title>Coffee – Forum</title>
<link rel="stylesheet" href="https://fonts.googleapis.com/css2?family=Yanone+Kaffeesatz:wght@500;600&family=Arimo:wght@400;700&display=swap">
<style>
:root{
  --bar:#6a431f;
  --bar-dark:#4e2f14;
  --tan:#d3a571;
  --tan-light:#dcb383;
  --paper:#f1f2f3;
  --rule:#9a9a9a;
  --title:#c4561c;
  --meta:#6c6c6c;
  --brown:#5a3717;
  --side-text:#5e3a18;
  --pill:#6b421c;
  --pill-text:#f3e3cf;
  --slider:#f29a22;
  --note:#ecd7a6;
  --footer:#5c3a18;
  --footer-link:#b88a5c;
}
*{box-sizing:border-box;margin:0;padding:0}
html,body{width:1200px;height:1200px;overflow:hidden}
body{position:relative;font-family:"Arimo",Arial,sans-serif;background:radial-gradient(ellipse at 40% 40%,var(--tan-light),var(--tan) 70%);color:var(--meta)}
.abs{position:absolute}
.topbar{left:0;top:0;width:1200px;height:30px;background:var(--bar)}
.account-links{left:217px;top:10px;font-size:10px;color:#e6cfb1;word-spacing:2px}
.field{top:5px;height:21px;border:1px solid #8a5e35;border-radius:3px;background:#5f3b19;color:#e8d4bb;font-size:10px;padding:5px 12px}
.field.email{left:654px;width:130px}
.field.pass{left:790px;width:130px;padding-left:22px}
.login{left:936px;top:5px;width:45px;height:21px;border:1px solid #8a5e35;border-radius:3px;background:#3e240c;color:#f2e4d2;font-size:10px;font-weight:700;text-align:center;line-height:19px}
.main-nav{top:48px;left:556px;display:flex;gap:0;font-family:"Yanone Kaffeesatz",sans-serif;font-weight:600;font-size:21px;color:#fff;letter-spacing:.5px;text-shadow:1px 1px 1px rgba(70,40,10,.6)}
.main-nav span{position:absolute;white-space:nowrap}
.brand{left:237px;top:62px;display:flex;align-items:center;gap:10px;font-size:40px;font-weight:700;color:var(--brown)}
.brand .dot{width:26px;height:26px;border-radius:50%;background:var(--brown)}
.results{left:629px;top:102px;width:354px;height:22px;background:var(--bar);border-radius:2px;color:#f3e3cf;font-size:10px;line-height:22px;padding-left:22px}
.board{left:216px;top:154px;width:566px;height:806px;background:var(--paper);box-shadow:0 1px 3px rgba(60,30,5,.35)}
.board-edge{left:216px;top:958px;width:566px;height:14px}
.topic{position:absolute;left:30px;width:520px;height:89px;border-bottom:1px solid var(--rule)}
.topic h3{position:absolute;left:24px;top:21px;font-size:11.5px;font-weight:700;color:var(--title);letter-spacing:.3px}
.topic .forum{position:absolute;left:24px;top:43px;font-size:10px;color:var(--meta)}
.topic .fresh{position:absolute;left:24px;top:62px;font-size:10px;color:var(--meta);letter-spacing:.2px}
.avatar{position:absolute;left:666px;top:14px;width:60px;height:60px;left:450px}
.avatar.photo{background:linear-gradient(160deg,#c9a163,#e2c4a6 50%,#3f6f5a)}
.avatar.photo2{background:linear-gradient(170deg,#7a4a2a,#e8c8b0 45%,#cfd7e8)}
.avatar.blank{background:#c3c3c3;width:65px;height:65px}
.avatar.sketch{background:#f4f4f4;border:1px solid #999}
.search{left:805px;top:153px;width:131px;height:20px;background:var(--pill);border-radius:3px;color:#e8d4bb;font-size:10px;padding:4px 19px}
.side h4{position:absolute;left:808px;font-size:15px;font-weight:700;color:var(--side-text);letter-spacing:.3px}
.side p{position:absolute;left:808px;font-size:10px;color:var(--side-text);letter-spacing:.2px}
.slider-track{left:820px;top:403px;width:140px;height:4px;background:var(--slider)}
.handle{top:396px;width:26px;height:18px;background:#fff;border-radius:2px;font-size:9px;color:#000;text-align:center;line-height:18px;box-shadow:0 0 2px rgba(0,0,0,.3)}
.note{left:799px;top:442px;width:171px;height:184px;background:radial-gradient(ellipse at 50% 40%,#f2e2b9,var(--note) 70%,#d9bb82);box-shadow:0 1px 3px rgba(60,30,5,.4);padding:26px 18px;font-size:9.6px;line-height:9.6px;color:#4b3416;text-align:justify}
.more{left:570px;top:986px;width:101px;height:19px;background:var(--pill);border-radius:3px;color:#f3e3cf;font-size:10px;text-align:center;line-height:19px}
.footer{left:0;top:1022px;width:1200px;height:178px;background:radial-gradient(ellipse at 50% 40%,#6a4520,var(--footer) 60%,#4a2c10)}
.footer-nav span{position:absolute;top:1056px;font-family:"Yanone Kaffeesatz",sans-serif;font-weight:600;font-size:19px;color:var(--footer-link);letter-spacing:.5px}
.copy{left:0;width:1236px;top:1157px;text-align:center;font-size:8px;color:#b88a5c;letter-spacing:.3px}
</style>
</head>
<body>
<div class="abs topbar"></div>
<div class="abs account-links">Setup my Account &nbsp;Forgot Password?</div>
<div class="abs field email">email or Phone number</div>
<div class="abs field pass">Password</div>
<div class="abs login">Login</div>

<nav class="abs main-nav">
  <span style="left:0">PRODUCTS</span>
  <span style="left:93px">SERVICES</span>
  <span style="left:179px">FORUMS</span>
  <span style="left:254px">HELP</span>
  <span style="left:314px">BLOG</span>
  <span style="left:370px">CONTACT</span>
</nav>

<div class="abs brand"><span class="dot"></span>Coffee</div>
<div class="abs results">There are 3188 total results, with 50 results per page.</div>

<section class="abs board">
  <div class="topic" style="top:0"><h3>Cannot send email now, try again</h3><div class="forum">BillBrew</div><div class="fresh">Freshness 10 hours, 6 minutes ago, Posts: 1</div><div class="avatar sketch" role="img" aria-label="Default sketched user avatar"></div></div>
  <div class="topic" style="top:89px"><h3>Missing product after payment</h3><div class="forum">HomeLister</div><div class="fresh">Freshness 12 hours, 10 minutes ago, Posts: 1</div><div class="avatar photo" role="img" aria-label="User profile photo"></div></div>
  <div class="topic" style="top:178px"><h3>Missing product after payment</h3><div class="forum">HomeLister</div><div class="fresh">Freshness 12 hours, 10 minutes ago, Posts: 1</div><div class="avatar photo" role="img" aria-label="User profile photo"></div></div>
  <div class="topic" style="top:267px"><h3>Missing product after payment</h3><div class="forum">HomeLister</div><div class="fresh">Freshness 12 hours, 10 minutes ago, Posts: 1</div><div class="avatar blank" role="img" aria-label="Default grey user avatar"></div></div>
  <div class="topic" style="top:356px"><h3>Missing product after payment</h3><div class="forum">HomeLister</div><div class="fresh">Freshness 12 hours, 10 minutes ago, Posts: 1</div><div class="avatar photo" role="img" aria-label="User profile photo"></div></div>
  <div class="topic" style="top:445px"><h3>Missing product after payment</h3><div class="forum">HomeLister</div><div class="fresh">Freshness 12 hours, 10 minutes ago, Posts: 1</div><div class="avatar blank" role="img" aria-label="Default grey user avatar"></div></div>
  <div class="topic" style="top:534px"><h3>Missing product after payment</h3><div class="forum">HomeLister</div><div class="fresh">Freshness 12 hours, 10 minutes ago, Posts: 1</div><div class="avatar photo" role="img" aria-label="User profile photo"></div></div>
  <div class="topic" style="top:623px"><h3>Missing product after payment</h3><div class="forum">HomeLister</div><div class="fresh">Freshness 12 hours, 10 minutes ago, Posts: 1</div><div class="avatar photo2" role="img" aria-label="User profile photo"></div></div>
  <div class="topic" style="top:712px"><h3>Missing product after payment</h3><div class="forum">HomeLister</div><div class="fresh">Freshness 12 hours, 10 minutes ago, Posts: 1</div><div class="avatar photo" role="img" aria-label="User profile photo"></div></div>
</section>
<svg class="abs board-edge" width="566" height="14" viewBox="0 0 566 14">
  <path d="M0 0H566V6L540 9 500 7 440 10 380 8 300 10 240 8 170 11 100 8 40 10 0 8Z" fill="#e8e6e2" stroke="#b9ab98" stroke-width="1"/>
</svg>

<div class="abs search">search topics...</div>
<div class="side">
  <h4 style="top:199px">Product</h4>
  <p style="top:223px">HomeLister2307</p>
  <p style="top:242px">BillBrew425</p>
  <p style="top:261px">The Summit Premium Theme270</p>
  <p style="top:280px">ClientCup186</p>
  <h4 style="top:305px">Topic Types</h4>
  <p style="top:329px">Regular2794</p>
  <p style="top:348px">Premium394</p>
  <h4 style="top:372px">Topic Posts</h4>
</div>
<div class="abs slider-track"></div>
<div class="abs handle" style="left:798px">1</div>
<div class="abs handle" style="left:957px">54</div>

<div class="abs note">This is a community forum for discussion of HomeLister, BillBrew, ClientCup, as well as general PressKit and web-related issues. If you are seeking support, you may ask questions directly to our staff by utilizing the Premium Question feature, or you can read more about our support policy.</div>

<div class="abs more">Load 50 more</div>

<footer class="abs footer"></footer>
<nav class="footer-nav">
  <span style="left:391px">HOME</span>
  <span style="left:469px">SERVICES</span>
  <span style="left:570px">PRODUCTS</span>
  <span style="left:678px">FORUM</span>
  <span style="left:764px">HELP</span>
</nav>
<div class="abs copy">©COPYRIGHTS 2012. ALL RIGHTS RESERVED</div>
</body>
</html>
```